GDFH Business Card

Looking for a business card design to incorporate our branding. We want to only use the colors listing in the Branding Package (attached).
Updates

Target Market(s)

People who need their phone or device fixed.

Industry/Entity Type

Electronics

Contact Information for Business Card

Please use:

Gadget Fix Haven LLC
4870 S Ridgecrest Pkwy
Suite 318
San Antonio, TX 78291

Wendell Thorsby, Store Manager

(210) 555-0147

Requirements
Must have
• Must include the colors that are contained within the Branding Package PDF file.

```html
<!DOCTYPE html>
<html lang="en">
<head>
<meta charset="utf-8">
<title>Gadget Fix Haven – Business Card</title>
<link rel="stylesheet" href="https://fonts.googleapis.com/css2?family=Oswald:wght@300;500&family=Roboto+Condensed:wght@300;400&display=swap">
<style>
  :root {
    --brand-orange: #f0532b;
    --card-dark: #1d1c20;
    --card-light: #ffffff;
    --ink-grey: #6b6b6e;
    --ink-soft: #8a8a8d;
    --rule-grey: #b9b9bb;
    --stage: #eceeed;
  }
  * { margin: 0; padding: 0; box-sizing: border-box; }
  html, body { width: 1200px; height: 750px; overflow: hidden; }
  body {
    background: var(--stage);
    display: flex;
    flex-direction: column;
    align-items: center;
    justify-content: center;
    gap: 40px;
    font-family: "Roboto Condensed", Arial, sans-serif;
  }
  .card {
    width: 560px;
    height: 320px;
    border-radius: 26px;
    position: relative;
    box-shadow: 0 6px 18px rgba(0,0,0,0.12);
  }
  .card--front {
    background: var(--card-dark);
    display: flex;
    align-items: center;
    justify-content: center;
  }
  .card--back { background: var(--card-light); }

  .brand {
    display: flex;
    align-items: center;
    gap: 14px;
  }
  .brand__square {
    width: 58px;
    height: 58px;
    border-radius: 10px;
    background: var(--brand-orange);
  }
  .brand__name {
    font-family: "Roboto Condensed", Arial, sans-serif;
    font-weight: 300;
    font-size: 44px;
    color: var(--brand-orange);
    letter-spacing: 0.5px;
  }
  .brand--small { gap: 9px; }
  .brand--small .brand__square { width: 30px; height: 30px; border-radius: 6px; }
  .brand--small .brand__name { font-size: 23px; }

  .identity {
    position: absolute;
    top: 60px;
    left: 40px;
    display: flex;
    align-items: center;
    gap: 22px;
  }
  .person { text-align: right; }
  .person__first {
    font-family: "Oswald", sans-serif;
    font-weight: 300;
    font-size: 36px;
    line-height: 1;
    color: var(--ink-grey);
    letter-spacing: 1px;
  }
  .person__last {
    font-family: "Oswald", sans-serif;
    font-weight: 500;
    font-size: 42px;
    line-height: 1.05;
    color: var(--brand-orange);
    letter-spacing: 1px;
  }
  .person__role {
    font-family: "Roboto Condensed", Arial, sans-serif;
    font-size: 11px;
    letter-spacing: 1.5px;
    color: var(--ink-grey);
    margin-top: 2px;
  }
  .divider {
    width: 1px;
    height: 100px;
    background: var(--rule-grey);
  }

  .contact {
    position: absolute;
    left: 40px;
    bottom: 34px;
    list-style: none;
    font-size: 16px;
    color: var(--ink-soft);
    line-height: 1.55;
  }
  .contact__item { display: flex; align-items: center; gap: 10px; }
  .contact__icon { width: 16px; height: 16px; flex: none; }

  .address {
    position: absolute;
    right: 40px;
    bottom: 34px;
    text-align: right;
    font-style: normal;
    font-size: 16px;
    line-height: 1.45;
    color: var(--ink-soft);
  }
</style>
</head>
<body>

  <section class="card card--front" aria-label="Business card front">
    <div class="brand">
      <span class="brand__square"></span>
      <span class="brand__name">Gadget Fix Haven</span>
    </div>
  </section>

  <section class="card card--back" aria-label="Business card back">
    <div class="identity">
      <div class="person">
        <p class="person__first">WENDELL</p>
        <p class="person__last">THORSBY</p>
        <p class="person__role">STORE MANAGER</p>
      </div>
      <span class="divider"></span>
      <div class="brand brand--small">
        <span class="brand__square"></span>
        <span class="brand__name">Gadget Fix Haven</span>
      </div>
    </div>

    <ul class="contact">
      <li class="contact__item">
        <svg class="contact__icon" viewBox="0 0 16 16" aria-hidden="true">
          <path d="M4 1.5 L6 4.5 L4.8 6 C5.6 8 8 10.4 10 11.2 L11.5 10 L14.5 12 L13 14.5 C7.5 14 2 8.5 1.5 3 Z" fill="none" stroke="var(--brand-orange)" stroke-width="1.3" stroke-linejoin="round"/>
        </svg>
        (210) 555-0147
      </li>
      <li class="contact__item">
        <svg class="contact__icon" viewBox="0 0 16 16" aria-hidden="true">
          <rect x="1.5" y="3.5" width="13" height="9" fill="none" stroke="var(--brand-orange)" stroke-width="1.3"/>
          <path d="M1.5 3.5 L8 9 L14.5 3.5" fill="none" stroke="var(--brand-orange)" stroke-width="1.3"/>
        </svg>
        hello@gadgetfixhaven.com
      </li>
      <li class="contact__item">
        <svg class="contact__icon" viewBox="0 0 16 16" aria-hidden="true">
          <circle cx="8" cy="8" r="6.5" fill="none" stroke="var(--brand-orange)" stroke-width="1.3"/>
          <ellipse cx="8" cy="8" rx="2.8" ry="6.5" fill="none" stroke="var(--brand-orange)" stroke-width="1.1"/>
          <path d="M1.5 8 H14.5" stroke="var(--brand-orange)" stroke-width="1.1"/>
        </svg>
        www.gadgetfixhaven.com
      </li>
    </ul>

    <address class="address">
      4870 S Ridgecrest Pkwy<br>
      Suite 318<br>
      San Antonio, TX 78291
    </address>
  </section>

</body>
</html>
```